TR Advisory Business Cards - High End AV / Low Voltage Company

We are low voltage AV company that specializes in high end clients on the residential side and larger businesses on the commercial side. We want something modern, tech looking but also something that is extremely professional looking. We have uploaded our logos and postcards we already have in the field. Along with a picture of one of our wrapped vans. Our website is at www.trvadvisory.example and our primary colors are the orange, green, grey and blue all military color finishes.

We are interesting in the slogans "Pairing You with the Right Technology" or "Leading the Lowcountry in Tech"

Target Market(s)

We focus on 70% Commercial and 30% Residential Customers

Industry/Entity Type

Low Voltage, AV Company

Contact Information for Business Card

Name - Dorian Fairweather, Title - Owner, Office Phone - 555-714-3096, Mobile Phone - 555-802-4173, E-Mail - d@trvadvisory.example, Website: www.trvadvisory.example

Font styles to use
Sans Serif

Requirements
Must have
• Must have Name, Title, Work Phone & Mobile, Website and Logo.
Nice to have
• We want something that will impress our higher end clients with a great logo
Should not have
• Too traditional or plain.

```html
<!DOCTYPE html>
<html lang="en">
<head>
<meta charset="utf-8">
<title>TR Advisory Business Cards</title>
<link href="https://fonts.googleapis.com/css2?family=Jost:wght@400;500;600&display=swap" rel="stylesheet">
<style>
  :root {
    --stage: #c6c6c6;
    --card: #ffffff;
    --orange: #ec6a37;
    --olive: #434a25;
    --ink: #3f4524;
    --muted: #5a5a52;
    --pattern-a: #fbfbfb;
    --pattern-b: #f0f0f0;
  }
  * { margin: 0; padding: 0; box-sizing: border-box; }
  html, body { width: 1200px; height: 1200px; overflow: hidden; }
  body {
    background: var(--stage);
    font-family: "Jost", sans-serif;
    position: relative;
  }
  .card {
    position: absolute;
    left: 226px;
    width: 750px;
    height: 458px;
    background: var(--card);
    overflow: hidden;
    box-shadow: 0 26px 30px -18px rgba(0,0,0,0.28);
  }
  .card--front { top: 92px; }
  .card--back { top: 633px; }

  /* Front */
  .front-texture {
    position: absolute; left: 0; top: 0; width: 750px; height: 363px;
    background: linear-gradient(180deg, var(--pattern-a), var(--pattern-b));
  }
  .front-band {
    position: absolute; left: 0; top: 363px; width: 750px; height: 95px;
    background: var(--olive);
  }
  .brand {
    position: absolute; left: 0; top: 150px; width: 750px;
    text-align: center;
    color: var(--orange);
    font-weight: 600;
    font-size: 64px;
    letter-spacing: 1px;
  }
  .tagline {
    position: absolute; left: 86px; top: 340px;
    width: 578px; height: 50px;
    background: var(--orange);
    border: 2px solid #fff;
    border-radius: 25px;
    color: #fff;
    font-weight: 500;
    font-size: 22px;
    line-height: 46px;
    text-align: center;
    letter-spacing: 0.2px;
  }

  /* Back */
  .spine {
    position: absolute; left: 77px; top: 0; width: 3px; height: 458px;
    background: var(--orange);
  }
  .person-badge {
    position: absolute; left: 47px; top: 61px; width: 62px; height: 71px;
    background: var(--orange);
  }
  .person-badge svg { position: absolute; left: 11px; top: 15px; }
  .name {
    position: absolute; left: 126px; top: 60px;
    font-size: 33px; font-weight: 500; color: var(--ink);
    letter-spacing: 0.5px;
  }
  .title {
    position: absolute; left: 127px; top: 101px;
    font-size: 25px; font-weight: 400; color: var(--muted);
    letter-spacing: 0.5px;
  }
  .contact-rail {
    position: absolute; left: 47px; top: 192px; width: 62px; height: 204px;
    background: var(--orange);
    border-radius: 31px;
  }
  .contact-rail svg { position: absolute; left: 0; top: 0; }
  .contact-list { list-style: none; }
  .contact-list li {
    position: absolute; left: 126px;
    font-size: 26px; color: var(--ink); line-height: 1;
  }
  .divider {
    position: absolute; width: 2px; background: var(--orange);
  }
  .photo {
    position: absolute; left: 518px; top: 139px; width: 182px; height: 182px;
    border-radius: 50%;
    border: 3px solid var(--orange);
    background: radial-gradient(circle at 50% 35%, #7e8a45 0%, #4d5a2c 50%, #3a3f2c 80%, #6b6a62 100%);
  }
</style>
</head>
<body>

<section class="card card--front">
  <div class="front-texture" role="img" aria-label="Faint light-grey circuit-board line pattern"></div>
  <div class="front-band"></div>
  <div class="brand">TR Advisory</div>
  <div class="tagline">PAIRING YOU WITH THE RIGHT TECHNOLOGY</div>
</section>

<section class="card card--back">
  <div class="spine"></div>

  <div class="person-badge">
    <svg width="40" height="40" viewBox="0 0 40 40">
      <circle cx="20" cy="20" r="19" fill="#434a25"/>
      <circle cx="20" cy="15" r="6" fill="#fff"/>
      <path d="M9 30c1.5-6 5.5-8 11-8s9.5 2 11 8z" fill="#fff"/>
    </svg>
  </div>
  <div class="name">Dorian Fairweather</div>
  <div class="title">Owner</div>

  <div class="contact-rail">
    <svg width="62" height="204" viewBox="0 0 62 204">
      <g fill="#434a25">
        <circle cx="31" cy="28" r="18"/>
        <circle cx="31" cy="78" r="18"/>
        <circle cx="31" cy="127" r="18"/>
        <circle cx="31" cy="174" r="18"/>
      </g>
      <path d="M25 19c1-1 2-1 3 0l2 3c1 1 0 2-1 3l-1 1c1 3 3 5 6 6l1-1c1-1 2-2 3-1l3 2c1 1 1 2 0 3l-2 2c-6 1-15-8-14-14z" fill="#fff"/>
      <rect x="26" y="68" width="10" height="19" rx="2" fill="none" stroke="#fff" stroke-width="2"/>
      <circle cx="31" cy="84" r="1" fill="#fff"/>
      <rect x="21" y="120" width="20" height="14" fill="none" stroke="#fff" stroke-width="2"/>
      <path d="M21 120l10 8 10-8M21 134l7-7M41 134l-7-7" fill="none" stroke="#fff" stroke-width="1.6"/>
      <g fill="none" stroke="#fff" stroke-width="1.6">
        <circle cx="31" cy="174" r="10"/>
        <ellipse cx="31" cy="174" rx="4.5" ry="10"/>
        <path d="M21 174h20M23 169h16M23 179h16"/>
      </g>
    </svg>
  </div>
  <ul class="contact-list">
    <li style="top:207px">555-714-3096</li>
    <li style="top:257px">555-802-4173</li>
    <li style="top:306px">d@trvadvisory.example</li>
    <li style="top:351px">www.trvadvisory.example</li>
  </ul>

  <div class="divider" style="left:459px; top:95px; height:268px;"></div>
  <div class="divider" style="left:444px; top:137px; height:185px;"></div>
  <div class="divider" style="left:473px; top:137px; height:185px;"></div>

  <div class="photo" role="img" aria-label="Photo of the company's wrapped olive-green service van parked on a driveway"></div>
</section>

</body>
</html>
```